Waste and recycling company seeks artwork design and branding for plastic ruler.

We require a very professional design for our marketing product 'Ruler'.
It will be on a white plastic ruler 315mm long and 39mm high.
0 – 30 on the top (in mm).
0 – 12 on the bottom (in inches).
Numbering in black (to be included as an example only) as it is already printed on the plastic stock.
3 colours. Red, Black, Harbor crewman blue (colour is Pantone 3155C)
Total workable text area –
Length 312mm
Height 24mm
We would need the artwork in a vector format, either .pdf or .eps

Version 1 - Try and fit all the following info onto it.

Dot points -
• Commercial waste and recycling
• Bulk clean up bins
• Document shredding
• Liquid waste

08 8394 7261
info@kestrelbins.com.au
www.kestrelbins.com.au

SA Family owned and operated.

Kestrel logo

With service YOU can measure
Backed by our 5 Star customer service guarantee

I would like dot points on the left side of ruler. Kestrel logo in the middle of the ruler or on the far right hand side.
If Kestrel logo is in the middle, then ‘with service you can measure backed by our customer service guarantee.' to the right

Version 2. If all this does not fit -
Try having no dot points and have on the left hand side
'SA Family Owned and Operated'
Underneath ‘Phone 08 8394 7261
Underneath website and email
Kestrel logo

Target Market(s)

business clients

Industry/Entity Type

Recycling

Requirements
Must have
• phone number, email, logo,

```html
<!DOCTYPE html>
<html lang="en">
<head>
<meta charset="utf-8">
<title>Kestrel Waste &amp; Recycling – Promotional Ruler</title>
<link rel="stylesheet" href="https://fonts.googleapis.com/css2?family=Arimo:ital,wght@0,400;0,700;1,400;1,700&display=swap">
<style>
  :root {
    --ink: #111111;
    --brand-red: #d71f26;
    --harbor-blue: #00707a;
    --ruler-white: #ffffff;
    --ruler-edge: #4a4a4a;
    --backdrop-centre: #ffffff;
    --backdrop-edge: #dcdcdc;
  }
  html, body {
    margin: 0;
    padding: 0;
    width: 1200px;
    height: 800px;
    overflow: hidden;
  }
  body {
    position: relative;
    background: radial-gradient(ellipse 75% 70% at 50% 50%, var(--backdrop-centre) 45%, var(--backdrop-edge) 100%);
    font-family: "Arimo", Arial, sans-serif;
    color: var(--ink);
  }
  .ruler-art {
    position: absolute;
    left: 0;
    top: 0;
    width: 1200px;
    height: 800px;
  }
  .scale-number { font-family: "Arimo", Arial, sans-serif; fill: var(--ink); }
  .scale-number--mm { font-size: 11px; }
  .scale-number--inch { font-size: 14px; }

  .service-list {
    position: absolute;
    left: 99px;
    top: 357px;
    margin: 0;
    padding: 0;
    list-style: none;
    font-size: 12.5px;
    line-height: 15px;
  }
  .service-list li::before {
    content: "";
    display: inline-block;
    width: 4px;
    height: 4px;
    border-radius: 50%;
    background: var(--brand-red);
    margin-right: 6px;
    vertical-align: 3px;
  }

  .contact-block {
    position: absolute;
    left: 420px;
    top: 361px;
    width: 354px;
    text-align: center;
  }
  .contact-block__tagline {
    margin: 0;
    font-size: 12.5px;
    font-style: italic;
    line-height: 15px;
  }
  .contact-block__phone {
    margin: 2px 0 0;
    font-size: 20px;
    font-weight: 700;
    line-height: 22px;
    color: var(--brand-red);
  }
  .contact-block__links {
    margin: 1px 0 0;
    font-size: 12.5px;
    line-height: 15px;
    color: var(--brand-red);
  }
  .contact-block__links span + span { margin-left: 18px; }

  .brand-block {
    position: absolute;
    left: 900px;
    top: 357px;
    width: 230px;
    text-align: center;
  }
  .brand-mark {
    display: flex;
    align-items: center;
    justify-content: center;
    gap: 8px;
    height: 42px;
  }
  .brand-mark__dot {
    width: 16px;
    height: 16px;
    border-radius: 50%;
    background: var(--harbor-blue);
  }
  .brand-mark__name {
    font-size: 27px;
    font-weight: 700;
    letter-spacing: 0.5px;
    color: var(--harbor-blue);
  }
  .brand-promise {
    margin: 8px 0 0;
    font-size: 8.5px;
    font-style: italic;
    line-height: 10.5px;
  }
  .brand-promise strong { font-weight: 700; }
</style>
</head>
<body>

<svg class="ruler-art" width="1200" height="800" viewBox="0 0 1200 800" aria-label="Ruler with millimetre and inch scales">
  <defs>
    <!-- metric scale -->
    <pattern id="tick-mm" x="58.5" y="318" width="3.553" height="20" patternUnits="userSpaceOnUse">
      <line x1="0.4" y1="0" x2="0.4" y2="7" stroke="#111" stroke-width="0.7"/>
    </pattern>
    <pattern id="tick-half-cm" x="58.5" y="318" width="17.765" height="20" patternUnits="userSpaceOnUse">
      <line x1="0.4" y1="0" x2="0.4" y2="10" stroke="#111" stroke-width="0.7"/>
    </pattern>
    <pattern id="tick-cm" x="58.5" y="318" width="35.53" height="20" patternUnits="userSpaceOnUse">
      <line x1="0.4" y1="0" x2="0.4" y2="14" stroke="#111" stroke-width="0.8"/>
    </pattern>
    <!-- imperial scale -->
    <pattern id="tick-sixteenth" x="61.5" y="430" width="5.625" height="25" patternUnits="userSpaceOnUse">
      <line x1="0.4" y1="25" x2="0.4" y2="20" stroke="#111" stroke-width="0.7"/>
    </pattern>
    <pattern id="tick-eighth" x="61.5" y="430" width="11.25" height="25" patternUnits="userSpaceOnUse">
      <line x1="0.4" y1="25" x2="0.4" y2="18" stroke="#111" stroke-width="0.7"/>
    </pattern>
    <pattern id="tick-quarter" x="61.5" y="430" width="22.5" height="25" patternUnits="userSpaceOnUse">
      <line x1="0.4" y1="25" x2="0.4" y2="15" stroke="#111" stroke-width="0.7"/>
    </pattern>
    <pattern id="tick-half-inch" x="61.5" y="430" width="45" height="25" patternUnits="userSpaceOnUse">
      <line x1="0.4" y1="25" x2="0.4" y2="12" stroke="#111" stroke-width="0.8"/>
    </pattern>
    <pattern id="tick-inch" x="61.5" y="430" width="90" height="25" patternUnits="userSpaceOnUse">
      <line x1="0.4" y1="25" x2="0.4" y2="2" stroke="#111" stroke-width="0.9"/>
    </pattern>
  </defs>

  <rect class="ruler-body" x="39.5" y="318.5" width="1116" height="136" fill="var(--ruler-white)" stroke="var(--ruler-edge)" stroke-width="1"/>

  <g class="scale-metric">
    <rect x="58.5" y="318" width="1067.5" height="20" fill="url(#tick-mm)"/>
    <rect x="58.5" y="318" width="1067.5" height="20" fill="url(#tick-half-cm)"/>
    <rect x="58.5" y="318" width="1067.5" height="20" fill="url(#tick-cm)"/>
    <g class="scale-number scale-number--mm">
      <text x="60" y="341">1</text><text x="95.5" y="341">2</text><text x="131" y="341">3</text>
      <text x="166.6" y="341">4</text><text x="202.1" y="341">5</text><text x="237.6" y="341">6</text>
      <text x="273.2" y="341">7</text><text x="308.7" y="341">8</text><text x="344.2" y="341">9</text>
      <text x="379.8" y="341">10</text><text x="415.3" y="341">11</text><text x="450.8" y="341">12</text>
      <text x="486.4" y="341">13</text><text x="521.9" y="341">14</text><text x="557.4" y="341">15</text>
      <text x="593" y="341">16</text><text x="628.5" y="341">17</text><text x="664" y="341">18</text>
      <text x="699.5" y="341">19</text><text x="735.1" y="341">20</text><text x="770.6" y="341">21</text>
      <text x="806.1" y="341">22</text><text x="841.7" y="341">23</text><text x="877.2" y="341">24</text>
      <text x="912.7" y="341">25</text><text x="948.3" y="341">26</text><text x="983.8" y="341">27</text>
      <text x="1019.3" y="341">28</text><text x="1054.9" y="341">29</text><text x="1090.4" y="341">30</text>
      <text x="1125.9" y="341">31</text>
    </g>
  </g>

  <g class="scale-imperial">
    <rect x="44" y="430" width="1099" height="25" fill="url(#tick-sixteenth)"/>
    <rect x="44" y="430" width="1099" height="25" fill="url(#tick-eighth)"/>
    <rect x="44" y="430" width="1099" height="25" fill="url(#tick-quarter)"/>
    <rect x="44" y="430" width="1099" height="25" fill="url(#tick-half-inch)"/>
    <rect x="44" y="430" width="1099" height="25" fill="url(#tick-inch)"/>
    <g class="scale-number scale-number--inch">
      <text x="63" y="444">1</text><text x="153" y="444">2</text><text x="243" y="444">3</text>
      <text x="333" y="444">4</text><text x="423" y="444">5</text><text x="513" y="444">6</text>
      <text x="603" y="444">7</text><text x="693" y="444">8</text><text x="783" y="444">9</text>
      <text x="873" y="444">10</text><text x="963" y="444">11</text><text x="1053" y="444">12</text>
    </g>
  </g>
</svg>

<ul class="service-list">
  <li>Commercial waste and recycling</li>
  <li>Bulk clean up bins</li>
  <li>Document shredding</li>
  <li>Liquid waste</li>
</ul>

<div class="contact-block">
  <p class="contact-block__tagline">SA Family owned and operated</p>
  <p class="contact-block__phone">08 8394 7261</p>
  <p class="contact-block__links"><span>info@kestrelbins.com.au</span><span>www.kestrelbins.com.au</span></p>
</div>

<div class="brand-block">
  <div class="brand-mark">
    <span class="brand-mark__dot"></span>
    <span class="brand-mark__name">KESTREL</span>
  </div>
  <p class="brand-promise">With service <strong>YOU</strong> can measure<br>Backed by our <strong>5 Star</strong> customer service guarantee</p>
</div>

</body>
</html>
```